" Não vendemos nossos serviços "no varejo". Somos chamados a participar de projetos de investimento no Brasil ainda na fase de concepção, sob acordo de confidencialidade, buscando alimentar a modelagem financeira com os inputs tributários que frequentemente são cruciais na definição de viabilidade do projeto. Também somos chamados por nossos clientes para avaliar ou alocar contratualmente riscos decorrentes de contingências fiscais, especialmente em fusões e aquisições de empresas. E, ainda, patrocinar defesas ou pleitos em processos administrativos ou judiciais, sempre tendo como parte adversária o fisco (federal, estadual ou municipal). Atuamos em um ambiente profissional onde ética, compliance, qualidade e comprometimento são premissas. O propósito de nossa empresa é a criação de valor de modo sustentável, em questões fiscais, para negócios empreendidos no Brasil. "

```html
<!DOCTYPE html>
<html lang="pt-BR">
<head>
<meta charset="utf-8">
<title>Moura Lins Teixeira Advogados — Placa</title>
<link rel="stylesheet" href="https://fonts.googleapis.com/css2?family=Roboto+Condensed:wght@300;400&family=Montserrat:wght@400&display=swap">
<style>
  :root {
    --bg: #e9e6e1;
    --plate: #2a3a7a;
    --plate-edge: #8b9cc8;
    --name: #b9c2dd;
    --white: #ffffff;
  }
  * { margin: 0; padding: 0; box-sizing: border-box; }
  html, body { width: 1200px; height: 1200px; overflow: hidden; background: var(--bg); }
  .canvas { position: relative; width: 1200px; height: 1200px; }
  .plate {
    position: absolute;
    left: 96px; top: 451px;
    width: 1013px; height: 312px;
    background: var(--plate);
    border: 6px solid var(--plate-edge);
    border-radius: 52px;
  }
  .brand-mark {
    position: absolute;
    left: 134px; top: 28px;
    font-family: "Roboto Condensed", sans-serif;
    font-weight: 300;
    font-size: 190px;
    line-height: 1;
    letter-spacing: 6px;
    color: var(--white);
  }
  .firm-name {
    position: absolute;
    left: 649px; top: 44px;
    font-family: "Roboto Condensed", sans-serif;
    font-weight: 300;
    font-size: 42px;
    line-height: 49px;
    letter-spacing: 1px;
    color: var(--name);
    text-transform: uppercase;
    list-style: none;
  }
  .contact-line {
    position: absolute;
    left: 0; right: 0; top: 244px;
    text-align: center;
    font-family: "Montserrat", sans-serif;
    font-weight: 400;
    font-size: 25px;
    letter-spacing: 4px;
    color: var(--white);
  }
</style>
</head>
<body>
  <main class="canvas">
    <section class="plate">
      <div class="brand-mark">MLT</div>
      <ul class="firm-name">
        <li>Moura</li>
        <li>Lins</li>
        <li>Teixeira</li>
        <li>Advogados</li>
      </ul>
      <p class="contact-line">(00) 0000-0000 | WWW.SEUSITE.COM.BR</p>
    </section>
  </main>
</body>
</html>
```